Lofton Vale one page flyer

We need a standard A4 size flyer for a new company called Lofton Vale. We are a construction material company and sell trims, crown mouldings, baseboards and panelings.
We would like to see the design with the following information:
1. Size: A4
2. Only one front page, no design need to display on back
3. Logo (Lofton Vale, see the attached EPS file)
4. Slogan: We offer high quality products for competitive prices.
5. Content please see the PDF file
6. The production has 2 category, one called "Crown Moulding", the other is "Wainscoting", Crown Moulding has 5 productions, wainscoting has 2 production(Details see PDF file)
6. We temporary only can provide low resolution images for 7 productions, only the winner will be provided with High Resolution images.
Look and feel
Each slider illustrates characteristics of the customer's brand and the style your logo design should communicate.

```html
<!DOCTYPE html>
<html lang="en">
<head>
<meta charset="utf-8">
<title>Lofton Vale – Flyer</title>
<link rel="stylesheet" href="https://fonts.googleapis.com/css2?family=Open+Sans:wght@400;600;700&family=Questrial&family=Raleway:wght@500;600&display=swap">
<style>
  :root{
    --slate:#5d6771;
    --coral:#e0836b;
    --mist:#d8dadd;
    --ink:#2b2e31;
    --paper:#ffffff;
    --room-light:#eceae6;
    --room-mid:#c9c6c0;
  }
  *{margin:0;padding:0;box-sizing:border-box}
  html,body{width:848px;height:1200px;overflow:hidden;background:var(--paper)}
  .flyer{position:relative;width:848px;height:1200px;overflow:hidden;font-family:"Open Sans",Arial,sans-serif;color:var(--ink)}

  .hero-photo{position:absolute;left:0;top:0;width:848px;height:470px;
    background:linear-gradient(180deg,var(--room-light) 0%,#e2dfda 55%,var(--room-mid) 100%)}
  .hero-panel{position:absolute;left:0;top:0;width:848px;height:470px}
  .brand{position:absolute;left:24px;top:208px;display:flex;align-items:center;gap:16px}
  .brand-square{width:54px;height:54px;background:var(--slate)}
  .brand-name{font-family:"Raleway",Arial,sans-serif;font-weight:500;font-size:40px;letter-spacing:2px;color:var(--slate);line-height:1}
  .brand-tag{position:absolute;left:95px;top:259px;font-family:"Raleway",Arial,sans-serif;font-weight:500;font-size:14px;letter-spacing:2.4px;color:var(--slate)}

  .accent-strip{position:absolute;left:0;top:468px;width:848px;height:15px;background:var(--coral)}
  .slogan-band{position:absolute;left:0;top:484px;width:848px;height:82px;background:var(--slate);
    display:flex;align-items:center;padding-left:18px}
  .slogan{font-family:"Questrial",Arial,sans-serif;font-size:32px;color:var(--paper);letter-spacing:.3px}

  .section-tab{position:absolute;top:584px;height:36px}
  .section-tab svg{position:absolute;inset:0}
  .section-tab span{position:relative;display:block;line-height:36px;font-family:"Questrial",Arial,sans-serif;font-size:23px;color:var(--paper)}
  .tab-crown{left:0;width:258px}
  .tab-crown span{padding-left:26px}
  .tab-wainscot{right:0;width:256px}
  .tab-wainscot span{padding-left:50px}

  .product{position:absolute;width:140px;text-align:center}
  .product-shot{margin:0 auto;width:96px;height:88px;border-radius:4px;
    background:linear-gradient(135deg,#f4f4f4 0%,#cfd1d3 60%,#8e9196 100%)}
  .product-shot.wood{background:linear-gradient(135deg,#f2ece2 0%,#e3d3b6 60%,#c9b08a 100%)}
  .product-name{margin-top:10px;font-size:8px;color:var(--ink);line-height:1.2;white-space:nowrap}
  .product-size{font-size:10px;font-weight:700;color:var(--ink);margin-top:4px}

  .hours{position:absolute;left:392px;top:845px;width:456px;height:178px;background:var(--mist)}
  .hours-corner{position:absolute;left:-1px;top:0}
  .hours-title{position:absolute;left:32px;top:10px;font-weight:700;font-size:23px;color:var(--slate)}
  .hours-rule{position:absolute;left:32px;right:0;top:48px;height:2px;background:var(--paper)}
  .hours-table{position:absolute;left:68px;top:62px;border-collapse:collapse;font-size:23px;color:var(--ink)}
  .hours-table th{text-align:left;font-weight:700;padding:0 20px 0 0;height:34px}
  .hours-table td{font-weight:400;height:34px}

  .footer{position:absolute;left:0;top:1029px;width:848px;height:171px;background:var(--slate);color:var(--paper)}
  .footer-name{position:absolute;left:18px;top:14px;font-weight:700;font-size:22px}
  .footer-label{position:absolute;left:18px;top:42px;font-size:20px}
  .footer-rule{position:absolute;left:18px;top:73px;width:268px;height:2px;background:#8c949b}
  .footer-address{position:absolute;left:18px;top:84px;font-size:22px;line-height:34px}
  .footer-address sup{font-size:13px;line-height:0}
  .contact{position:absolute;left:458px;top:8px}
  .contact-label{font-size:20px}
  .contact-phone{font-weight:600;font-size:50px;line-height:1.05;letter-spacing:.5px}
  .contact-email{font-weight:600;font-size:31px;margin-left:12px;margin-top:2px}
</style>
</head>
<body>
<main class="flyer">

  <div class="hero-photo" role="img" aria-label="Photo of a bright empty room with white wainscoting panels, crown moulding, arched windows and a hanging lantern"></div>
  <svg class="hero-panel" viewBox="0 0 848 470" aria-hidden="true">
    <polygon points="0,150 405,66 366,410 0,440" fill="#ffffff" opacity="0.35"/>
    <polygon points="0,170 392,74 356,404 0,432" fill="#ffffff"/>
  </svg>
  <div class="brand">
    <div class="brand-square"></div>
    <div class="brand-name">LOFTON VALE</div>
  </div>
  <div class="brand-tag">FOR ALL TYPES OF PROJECTS</div>

  <div class="accent-strip"></div>
  <div class="slogan-band"><p class="slogan">We offer high quality products for competitive prices..</p></div>

  <div class="section-tab tab-crown">
    <svg viewBox="0 0 258 36" preserveAspectRatio="none"><polygon points="0,0 258,0 232,36 0,36" fill="var(--slate)"/></svg>
    <span>Crown Moulding</span>
  </div>
  <div class="section-tab tab-wainscot">
    <svg viewBox="0 0 256 36" preserveAspectRatio="none"><polygon points="0,0 256,0 256,36 28,36" fill="var(--slate)"/></svg>
    <span>Wainscoting</span>
  </div>

  <div class="product" style="left:2px;top:660px">
    <div class="product-shot" role="img" aria-label="Verona 9 crown moulding profile"></div>
    <p class="product-name">Verona 9 Crown Moulding</p>
    <p class="product-size">8 5/16"x5/8"</p>
  </div>
  <div class="product" style="left:116px;top:660px">
    <div class="product-shot" role="img" aria-label="Verona 8 crown moulding profile"></div>
    <p class="product-name">Verona 8 Crown Moulding</p>
    <p class="product-size">7 1/2"x5/8"</p>
  </div>
  <div class="product" style="left:236px;top:660px">
    <div class="product-shot" role="img" aria-label="Verona 7 crown moulding profile"></div>
    <p class="product-name">Verona 7 Crown Moulding</p>
    <p class="product-size">6 3/8"x5/8"</p>
  </div>
  <div class="product" style="left:508px;top:660px">
    <div class="product-shot wood" role="img" aria-label="Heritage chair rail profile"></div>
    <p class="product-name">Heritage Chair Rail</p>
    <p class="product-size">3 1/8"x7/8"</p>
  </div>
  <div class="product" style="left:636px;top:660px">
    <div class="product-shot wood" role="img" aria-label="Heritage panel mould profile and wood sample"></div>
    <p class="product-name">Heritage Panel Mould</p>
    <p class="product-size">1 5/8"x1/2"</p>
  </div>

  <div class="product" style="left:2px;top:842px">
    <div class="product-shot" role="img" aria-label="Aster 8 crown moulding profile"></div>
    <p class="product-name">Aster 8 Crown Moulding</p>
    <p class="product-size">7 5/8"x5/8"</p>
  </div>
  <div class="product" style="left:130px;top:842px">
    <div class="product-shot" role="img" aria-label="Aster 6 crown moulding profile"></div>
    <p class="product-name">Aster 6 Crown Moulding</p>
    <p class="product-size">6 1/8"x5/8"</p>
  </div>

  <section class="hours">
    <svg class="hours-corner" width="30" height="60" viewBox="0 0 30 60" aria-hidden="true"><polygon points="0,0 30,0 0,40" fill="#ffffff"/></svg>
    <h2 class="hours-title">Office Hours</h2>
    <div class="hours-rule"></div>
    <table class="hours-table">
      <tr><th>Mon – Fri</th><td>7:00am – 6.00pm</td></tr>
      <tr><th>Saturdays</th><td>8:00am – 4.00pm</td></tr>
      <tr><th>Sundays</th><td>Closed</td></tr>
    </table>
  </section>

  <footer class="footer">
    <p class="footer-name">Lofton Vale</p>
    <p class="footer-label">Office:</p>
    <div class="footer-rule"></div>
    <p class="footer-address">417 12<sup>th</sup> ave, unit 2<br>Maple Ridge, Ontario L5C 2K8</p>
    <div class="contact">
      <p class="contact-label">Call Us:</p>
      <p class="contact-phone">905-555-0142</p>
      <p class="contact-email">info@loftonvale.ca</p>
    </div>
  </footer>

</main>
</body>
</html>
```